Brannock Bay Ferry and Haulage

Need to redesign our business cards to relay that we do freight logistics and water taxi service. We also work with gov. agencies doing environmental clean up, oil spill response, remote site construction and work with many of the air taxi and helicopter services on Kodiak Island. Out website is www.brannockbayferry.com to get a better idea of what we do.

Contact Information for Business Card

I have a previous business card but it just has the logo on the front, and a sunset picture on the back with the contact info. It does not relay what we do and what we can help with. I like a simple straight forward design over a busy one.

Colors
3176b5
0455a3
cfdfed

Requirements
Must have
• logo, email, website, phone number

```html
<!DOCTYPE html>
<html lang="en">
<head>
<meta charset="utf-8">
<title>Brannock Bay Ferry and Haulage – Business Cards</title>
<link rel="stylesheet" href="https://fonts.googleapis.com/css2?family=Montserrat:wght@700&family=Questrial&display=swap">
<style>
  :root {
    --blue-deep: #0455a3;
    --blue-mid: #3176b5;
    --blue-pale: #cfdfed;
    --ink: #1c1c1c;
    --ink-soft: #8a8a8a;
    --card: #f7f7f7;
    --backdrop: #e6e8eb;
  }
  * { margin: 0; padding: 0; box-sizing: border-box; }
  html, body {
    width: 1200px; height: 900px; overflow: hidden;
    background: var(--backdrop);
  }
  .sheet { position: relative; width: 1200px; height: 900px; }
  .card {
    position: absolute; left: 250px; width: 700px; height: 400px;
    background: var(--card);
    overflow: hidden;
    box-shadow: 0 6px 18px rgba(0,0,0,0.12);
  }
  .card--contact { top: 40px; }
  .card--brand { top: 470px; }
  .card__waves { position: absolute; inset: 0; width: 700px; height: 400px; }
  .wordmark {
    position: absolute;
    display: flex; align-items: center; gap: 12px;
    font-family: "Questrial", sans-serif;
    color: var(--blue-deep);
  }
  .wordmark__dot { flex: none; border-radius: 50%; background: var(--blue-mid); }
  .wordmark__name { line-height: 1.1; }
  .card--contact .wordmark { left: 56px; top: 92px; }
  .card--contact .wordmark__dot { width: 26px; height: 26px; }
  .card--contact .wordmark__name { font-size: 25px; }
  .card--brand .wordmark { left: 0; right: 0; top: 110px; justify-content: center; }
  .card--brand .wordmark__dot { width: 38px; height: 38px; }
  .card--brand .wordmark__name { font-size: 36px; }
  .person { position: absolute; left: 392px; top: 64px; }
  .person__name {
    font-family: "Montserrat", sans-serif; font-weight: 700;
    font-size: 31px; color: var(--ink); letter-spacing: 0.2px;
  }
  .person__role {
    font-family: "Questrial", sans-serif;
    font-size: 19px; color: var(--ink-soft); margin-top: 2px;
  }
  .contact-list {
    position: absolute; left: 58px; top: 218px; list-style: none;
    font-family: "Questrial", sans-serif; font-size: 17px; color: var(--ink);
  }
  .contact-list__item { display: flex; align-items: center; gap: 14px; height: 30px; }
  .contact-list__icon { width: 16px; height: 16px; fill: var(--blue-deep); flex: none; }
</style>
</head>
<body>
<main class="sheet">

  <section class="card card--contact" aria-label="Business card, contact side">
    <svg class="card__waves" viewBox="0 0 700 400" aria-hidden="true">
      <path d="M0 372 C160 392 310 378 430 316 C530 262 590 170 700 140 L700 400 L0 400 Z" fill="var(--blue-pale)"/>
      <path d="M460 400 C560 330 610 250 700 222 L700 400 Z" fill="var(--blue-mid)"/>
    </svg>

    <div class="wordmark">
      <span class="wordmark__dot"></span>
      <span class="wordmark__name">Brannock Bay<br>Ferry and Haulage</span>
    </div>

    <div class="person">
      <h1 class="person__name">Marek Ellison</h1>
      <p class="person__role">Digital Designer</p>
    </div>

    <ul class="contact-list">
      <li class="contact-list__item">
        <svg class="contact-list__icon" viewBox="0 0 16 16" aria-hidden="true"><path d="M3.2 1.2l2.4 0.2 1 3.2-1.6 1.2c0.8 1.8 2.2 3.2 4 4l1.2-1.6 3.2 1 0.2 2.4c-0.6 1.4-2 2.2-3.4 2-4.8-0.8-8.2-4.2-9-9-0.2-1.4 0.6-2.8 2-3.4z"/></svg>
        <span>907-555-0142</span>
      </li>
      <li class="contact-list__item">
        <svg class="contact-list__icon" viewBox="0 0 16 16" aria-hidden="true"><path d="M1 3h14v1.2L8 8.6 1 4.2z M1 5.8l7 4.4 7-4.4V13H1z"/></svg>
        <span>brannockbayferry@mailbox.com</span>
      </li>
      <li class="contact-list__item">
        <svg class="contact-list__icon" viewBox="0 0 16 16" aria-hidden="true"><path d="M8 1a7 7 0 1 0 0 14A7 7 0 0 0 8 1zm0 1.4c0.9 0.9 1.6 2.4 1.8 4.1H6.2C6.4 4.8 7.1 3.3 8 2.4zM2.5 6.5c0.4-1.8 1.7-3.2 3.3-3.8-0.6 1-1 2.3-1.1 3.8zm0 3h2.2c0.1 1.5 0.5 2.8 1.1 3.8-1.6-0.6-2.9-2-3.3-3.8zM8 13.6c-0.9-0.9-1.6-2.4-1.8-4.1h3.6c-0.2 1.7-0.9 3.2-1.8 4.1zm2.2-0.3c0.6-1 1-2.3 1.1-3.8h2.2c-0.4 1.8-1.7 3.2-3.3 3.8zm1.1-6.8c-0.1-1.5-0.5-2.8-1.1-3.8 1.6 0.6 2.9 2 3.3 3.8z"/></svg>
        <span>www.brannockbayferry.com</span>
      </li>
    </ul>
  </section>

  <section class="card card--brand" aria-label="Business card, brand side">
    <svg class="card__waves" viewBox="0 0 700 400" aria-hidden="true">
      <path d="M0 240 C30 330 140 372 700 372 L700 400 L0 400 Z" fill="var(--blue-pale)"/>
      <path d="M0 285 C50 360 180 382 470 364 C300 390 120 400 0 400 Z" fill="var(--blue-deep)"/>
      <path d="M470 390 C580 386 650 376 700 366 L700 382 C650 390 580 396 470 396 Z" fill="var(--blue-mid)"/>
    </svg>
    <svg class="card__waves" viewBox="0 0 700 400" role="img" aria-label="Illustration area: ferry boat cutting through the waves">
      <defs>
        <linearGradient id="ferry-area-fill" x1="0" y1="0" x2="1" y2="1">
          <stop offset="0" stop-color="#cfdfed"/>
          <stop offset="1" stop-color="#0455a3"/>
        </linearGradient>
      </defs>
      <rect x="400" y="240" width="300" height="120" fill="url(#ferry-area-fill)"/>
    </svg>

    <div class="wordmark">
      <span class="wordmark__dot"></span>
      <span class="wordmark__name">Brannock Bay<br>Ferry and Haulage</span>
    </div>
  </section>

</main>
</body>
</html>
```